Letterhead and Envelope Design for Investment Company

We need a letterhead and envelope design.
We are a family owned investment company doing direct investments into other family owned businesses.
I have attached all our current marketing material including our logo for reference.

Our under construction website can be found here:
https://owen-darby-qk7m.sitebrella.example/
password: Marrowdale

Target Market(s)

Bankers, business owners, financial partners

Industry/Entity Type

Investment

Colors

Designer to choose colors to be used in the design.

Requirements
Must have
• Logo, and company information

```html
<!DOCTYPE html>
<html lang="en">
<head>
<meta charset="utf-8">
<title>Marrowdale Holdings Inc — Letterhead and Envelopes</title>
<link href="https://fonts.googleapis.com/css2?family=Open+Sans:wght@400;600&display=swap" rel="stylesheet">
<style>
  :root {
    --backdrop: #5e3817;
    --paper: #ffffff;
    --gold: #c49a2c;
    --gold-bright: #e2bb3c;
    --flap-gold: #bc8e31;
    --ink: #2b2b2b;
    --band: #161616;
  }
  * { margin: 0; padding: 0; box-sizing: border-box; }
  html, body { width: 1200px; height: 740px; overflow: hidden; background: var(--backdrop); }
  body { position: relative; font-family: "Open Sans", Arial, sans-serif; color: var(--ink); }

  .sheet { position: absolute; background: var(--paper); box-shadow: 3px 4px 6px rgba(0,0,0,.45); overflow: hidden; }

  .brand { position: absolute; text-align: center; font-family: "Open Sans", Arial, sans-serif; font-weight: 600; color: var(--gold); line-height: 1; }
  .brand-name { display: block; letter-spacing: .02em; text-transform: uppercase; white-space: nowrap; }
  .brand-sub { display: flex; align-items: center; gap: 6px; justify-content: center; margin-top: 3px; }
  .brand-sub::before, .brand-sub::after { content: ""; flex: 1; height: 1px; background: currentColor; }

  .contact { position: absolute; font-size: 7.5px; line-height: 11px; white-space: nowrap; }
  .contact-line { display: flex; align-items: center; gap: 4px; }
  .contact svg { width: 7px; height: 7px; fill: var(--gold); flex: none; }

  /* Letterhead */
  .letterhead { left: 56px; top: 56px; width: 486px; height: 628px; }
  .letterhead .brand { left: 143px; top: 90px; width: 200px; }
  .letterhead .brand-name { font-size: 13px; }
  .letterhead .brand-sub { font-size: 8px; }
  .letterhead .rule { position: absolute; left: 24px; right: 18px; top: 574px; height: 1px;
    background: linear-gradient(90deg, var(--gold-bright) 0 46%, transparent 46% 47.5%, var(--gold-bright) 47.5%); opacity: .7; }
  .letterhead .contact-left { left: 24px; top: 580px; }
  .letterhead .web { left: 190px; top: 586px; color: var(--gold); letter-spacing: .03em; }
  .letterhead .address { right: 18px; top: 582px; text-align: right; }
  .gold-line { position: absolute; left: 0; right: 0; height: 3px;
    background: linear-gradient(90deg, #b88a25, var(--gold-bright) 50%, #b88a25); }
  .dark-band { position: absolute; left: 0; right: 0; bottom: 0; background: var(--band); }
  .letterhead .gold-line { top: 604px; }
  .letterhead .dark-band { height: 21px; }

  /* Envelope back */
  .envelope-back { left: 588px; top: 120px; width: 554px; height: 250px; }
  .flap { position: absolute; left: 0; top: 0; width: 554px; height: 66px; }
  .envelope-back .brand { left: 197px; top: 38px; width: 160px; color: #fff; }
  .envelope-back .brand-name { font-size: 10px; }
  .envelope-back .brand-sub { font-size: 6px; margin-top: 2px; }

  /* Envelope front */
  .envelope-front { left: 587px; top: 394px; width: 555px; height: 250px; }
  .envelope-front .brand { left: 22px; top: 198px; width: 168px; }
  .envelope-front .brand-name { font-size: 11.5px; }
  .envelope-front .brand-sub { font-size: 7px; }
  .envelope-front .contact-mid { left: 209px; top: 184px; color: var(--gold); }
  .envelope-front .contact-mid .web { color: var(--ink); font-weight: 600; letter-spacing: .03em; }
  .envelope-front .address { left: 362px; top: 198px; color: var(--gold); }
  .envelope-front .gold-line { top: 228px; }
  .envelope-front .dark-band { height: 19px; }
</style>
</head>
<body>

<section class="sheet letterhead" aria-label="Letterhead">
  <div class="brand">
    <span class="brand-name">Marrowdale Holdings</span>
    <span class="brand-sub">INC</span>
  </div>
  <div class="rule"></div>
  <div class="contact contact-left">
    <div class="contact-line"><svg viewBox="0 0 10 10"><path d="M2 0h2l1 3-1.5 1a6 6 0 0 0 2.5 2.5L7 5l3 1v2c0 1-1 2-2 2A8 8 0 0 1 0 2c0-1 1-2 2-2z"/></svg>555 014 0392</div>
    <div class="contact-line"><svg viewBox="0 0 10 10"><path d="M0 2h10v6H0zM0 2l5 3.5L10 2" stroke="#fff" stroke-width=".8"/></svg>owen.darby@marrowdale.example</div>
  </div>
  <div class="contact web">www.marrowdale.example</div>
  <div class="contact address">48 Linden Ave, Suite 210<br>Fairbrook, IA 50012</div>
  <div class="gold-line"></div>
  <div class="dark-band"></div>
</section>

<section class="sheet envelope-back" aria-label="Envelope back">
  <svg class="flap" viewBox="0 0 554 66" aria-hidden="true">
    <path d="M0 0H554L530 50Q522 64 500 64H56Q34 64 24 50Z" fill="var(--flap-gold)"/>
  </svg>
  <div class="brand">
    <span class="brand-name">Marrowdale Holdings</span>
    <span class="brand-sub">INC</span>
  </div>
</section>

<section class="sheet envelope-front" aria-label="Envelope front">
  <div class="brand">
    <span class="brand-name">Marrowdale Holdings</span>
    <span class="brand-sub">INC</span>
  </div>
  <div class="contact contact-mid">
    <div class="contact-line"><svg viewBox="0 0 10 10"><path d="M2 0h2l1 3-1.5 1a6 6 0 0 0 2.5 2.5L7 5l3 1v2c0 1-1 2-2 2A8 8 0 0 1 0 2c0-1 1-2 2-2z"/></svg>555 014 0392</div>
    <div class="contact-line"><svg viewBox="0 0 10 10"><path d="M0 2h10v6H0zM0 2l5 3.5L10 2" stroke="#fff" stroke-width=".8"/></svg>owen.darby@marrowdale.example</div>
    <div class="contact-line web"><svg viewBox="0 0 10 10"><circle cx="5" cy="5" r="4.5"/><path d="M0.5 5h9M5 .5v9" stroke="#fff" stroke-width=".7"/></svg>www.marrowdale.example</div>
  </div>
  <div class="contact address">48 Linden Ave, Suite 210<br>Fairbrook, IA 50012</div>
  <div class="gold-line"></div>
  <div class="dark-band"></div>
</section>

</body>
</html>
```